Creative, Fun, Eye catching signage for new office - inspire and inform!

I am looking for a billboard sign, a smaller sign and a very small sign for parking spots. These will be located in our new office space. I have uploaded two logos, this way you can choose. I would love to see what it looks like with black behind the logo but am open to creative ideas. I would like the majority of the background to be black and/or white

1. Sign for over door – with five at the top like in the photo attached

The sign size is 2600mm (L) x 900mm (H)

Logo at the top then services to the right side
Social & Living Skills Programs
Support Workers
Respite/Supported Holidays
Exercise Physiology
Occupational Therapy
Speech Therapy
Psychology
Behavioural Therapy

I would like the design to tie in with the website and/or flyers/banners attached. Please also try and add 1800 452 917

2. Sign for glass roller door

745cm wide by 725cm high ( similar to what next door has without it saying parent )

Tellwick Logo
Drop Off Zone

Smaller signs for parking spots
1000cm wide, 60cm high

Tellwick logo Visitor Parking 24/7

I would like the design to be consistent across the three items so they work together but are not identical.

I have attached images showing what I am talking about in relation to the location of each sign.

Target Market(s)

Families, parents and people with disabilities

Industry/Entity Type

Disability and community service

Colors

Designer to choose colors to be used in the design.

Requirements
Must have
• White or black background - the logo and please use colours shown in the brochures and banners provided. Preferences are black white and yellow
Nice to have
• all of our services and website and/or 1800 452 917 on banner 1
Should not have
• I dont want it to be to busy please

```html
<!DOCTYPE html>
<html lang="en">
<head>
<meta charset="utf-8">
<title>Tellwick – Door Sign Options</title>
<link rel="stylesheet" href="https://fonts.googleapis.com/css2?family=Arimo:ital,wght@0,400;0,700;1,700&display=swap">
<style>
  :root {
    --backdrop: #e6e6e6;
    --ink: #000000;
    --paper: #ffffff;
    --soft-white: #e6e6e6;
    --sun-yellow: #f2d53c;
  }
  html, body {
    margin: 0;
    padding: 0;
    width: 1200px;
    height: 1200px;
    overflow: hidden;
    background: var(--backdrop);
  }
  .board {
    display: block;
    width: 1200px;
    height: 1200px;
    font-family: "Arimo", Arial, sans-serif;
  }
  .sheet-title { font-size: 80px; fill: var(--ink); }
  .sign-light .panel { fill: var(--paper); stroke: var(--ink); stroke-width: 4; }
  .sign-dark .panel { fill: var(--ink); }
  .door-number { font-size: 158px; font-weight: 700; text-anchor: middle; }
  .sign-light .door-number, .sign-light .brand-name, .sign-light .services { fill: var(--ink); }
  .sign-dark .door-number, .sign-dark .brand-name { fill: var(--soft-white); }
  .sign-dark .services { fill: var(--paper); }
  .services { font-size: 19.5px; }
  .services .services-heading { font-weight: 700; }
  .brand-mark { fill: var(--sun-yellow); }
  .brand-name { font-size: 64px; font-weight: 700; text-anchor: middle; letter-spacing: 1px; }
  .url-pill { fill: var(--sun-yellow); }
  .url-text { font-size: 34px; font-weight: 700; font-style: italic; fill: var(--ink); text-anchor: middle; }
</style>
</head>
<body>
<svg class="board" viewBox="0 0 1932 1932" xmlns="http://www.w3.org/2000/svg">
  <defs>
    <path id="sign-shape" d="M0 105 H309 A114 105 0 0 1 537 105 H846 V398 H0 Z"/>
    <g id="service-list">
      <tspan x="0" dy="21.2">Social &amp; Living Skills Programs</tspan>
      <tspan x="0" dy="21.2">Weekend &amp; Friday Night Socials</tspan>
      <tspan x="0" dy="21.2">Support Workers</tspan>
    </g>
  </defs>

  <text class="sheet-title" x="50" y="106">Sign 1</text>

  <!-- Option A: white with full logo -->
  <g class="sign-light" transform="translate(96 541)">
    <use href="#sign-shape" class="panel"/>
    <text class="door-number" x="423" y="136">5</text>
    <circle class="brand-mark" cx="292" cy="205" r="26"/>
    <text class="brand-name" x="220" y="312">TELLWICK</text>
    <rect class="url-pill" x="58" y="331" width="324" height="43" rx="20"/>
    <text class="url-text" x="220" y="365">tellwick.com.au</text>
    <text class="services" x="497" y="159">
      <tspan class="services-heading" x="497">OUR SERVICES:</tspan>
      <tspan x="497" dy="21.2">Social &amp; Living Skills Programs</tspan>
      <tspan x="497" dy="21.2">Weekend &amp; Friday Night Socials</tspan>
      <tspan x="497" dy="21.2">Support Workers</tspan>
      <tspan x="497" dy="21.2">Respite/Supported Holiday Stays/STA</tspan>
      <tspan x="497" dy="21.2">Exercise Physiology</tspan>
      <tspan x="497" dy="21.2">Occupational Therapy</tspan>
      <tspan x="497" dy="21.2">Speech Therapy</tspan>
      <tspan x="497" dy="21.2">Psychology</tspan>
      <tspan x="497" dy="21.2">Behavioral Therapy</tspan>
      <tspan x="497" dy="21.2">Sensorimotor Therapy</tspan>
    </text>
  </g>

  <!-- Option B: black with full logo -->
  <g class="sign-dark" transform="translate(990 541)">
    <use href="#sign-shape" class="panel"/>
    <text class="door-number" x="423" y="136">5</text>
    <circle class="brand-mark" cx="292" cy="205" r="26"/>
    <text class="brand-name" x="220" y="312">TELLWICK</text>
    <rect class="url-pill" x="58" y="331" width="324" height="43" rx="20"/>
    <text class="url-text" x="220" y="365">tellwick.com.au</text>
    <text class="services" x="497" y="159">
      <tspan class="services-heading" x="497">OUR SERVICES</tspan>
      <tspan x="497" dy="21.2">Social &amp; Living Skills Programs</tspan>
      <tspan x="497" dy="21.2">Weekend &amp; Friday Night Socials</tspan>
      <tspan x="497" dy="21.2">Support Workers</tspan>
      <tspan x="497" dy="21.2">Respite/Supported Holiday Stays/STA</tspan>
      <tspan x="497" dy="21.2">Exercise Physiology</tspan>
      <tspan x="497" dy="21.2">Occupational Therapy</tspan>
      <tspan x="497" dy="21.2">Speech Therapy</tspan>
      <tspan x="497" dy="21.2">Psychology</tspan>
      <tspan x="497" dy="21.2">Behavioral Therapy</tspan>
      <tspan x="497" dy="21.2">Sensorimotor Therapy</tspan>
    </text>
  </g>

  <!-- Option C: white with large mark -->
  <g class="sign-light" transform="translate(96 992)">
    <use href="#sign-shape" class="panel"/>
    <text class="door-number" x="423" y="136">5</text>
    <circle class="brand-mark" cx="218" cy="188" r="44"/>
    <text class="brand-name" x="218" y="298" style="font-size:50px">TELLWICK</text>
    <rect class="url-pill" x="56" y="331" width="324" height="43" rx="20"/>
    <text class="url-text" x="218" y="365">tellwick.com.au</text>
    <text class="services" x="497" y="159">
      <tspan class="services-heading" x="497">OUR SERVICES:</tspan>
      <tspan x="497" dy="21.2">Social &amp; Living Skills Programs</tspan>
      <tspan x="497" dy="21.2">Weekend &amp; Friday Night Socials</tspan>
      <tspan x="497" dy="21.2">Support Workers</tspan>
      <tspan x="497" dy="21.2">Respite/Supported Holiday Stays/STA</tspan>
      <tspan x="497" dy="21.2">Exercise Physiology</tspan>
      <tspan x="497" dy="21.2">Occupational Therapy</tspan>
      <tspan x="497" dy="21.2">Speech Therapy</tspan>
      <tspan x="497" dy="21.2">Psychology</tspan>
      <tspan x="497" dy="21.2">Behavioral Therapy</tspan>
      <tspan x="497" dy="21.2">Sensorimotor Therapy</tspan>
    </text>
  </g>

  <!-- Option D: black with large mark -->
  <g class="sign-dark" transform="translate(990 992)">
    <use href="#sign-shape" class="panel"/>
    <text class="door-number" x="423" y="136">5</text>
    <circle class="brand-mark" cx="207" cy="188" r="44"/>
    <text class="brand-name" x="207" y="298" style="font-size:50px">TELLWICK</text>
    <rect class="url-pill" x="45" y="331" width="324" height="43" rx="20"/>
    <text class="url-text" x="207" y="365">tellwick.com.au</text>
    <text class="services" x="497" y="159">
      <tspan class="services-heading" x="497">OUR SERVICES</tspan>
      <tspan x="497" dy="21.2">Social &amp; Living Skills Programs</tspan>
      <tspan x="497" dy="21.2">Weekend &amp; Friday Night Socials</tspan>
      <tspan x="497" dy="21.2">Support Workers</tspan>
      <tspan x="497" dy="21.2">Respite/Supported Holiday Stays/STA</tspan>
      <tspan x="497" dy="21.2">Exercise Physiology</tspan>
      <tspan x="497" dy="21.2">Occupational Therapy</tspan>
      <tspan x="497" dy="21.2">Speech Therapy</tspan>
      <tspan x="497" dy="21.2">Psychology</tspan>
      <tspan x="497" dy="21.2">Behavioral Therapy</tspan>
      <tspan x="497" dy="21.2">Sensorimotor Therapy</tspan>
    </text>
  </g>
</svg>
</body>
</html>
```